Audit/Compliance company needs Business Card Template

We are after a Business Card Template that we can modify internally to update details as people change positions.
We are an Australian based company specalising in Auditing and Quality/OHS systems development. - See www.kelvaranorth.com.au for more information
We would like the desings to be based around our logo and colours assocaited with it (attached for your information) however we are very open as to how the cards are designed.
We are looking for something quite edgy and mordern but it must have a professional/compliance feel to it (if possible).
The main details we would like to include within the card template are:
Name
Position Title
Postal Address
Phone Number
Mobile Number
Email Address
Website
The cards will be printed through tally press on Glossy paper so it should reflect the requirements below
Full Bleed Size (starting document size)
90 x 52 mm
1062 x 615 pixels
Document Trim Size (final size after being cut)
87 x 49 mm
1028 x 579 pixels
Resolution
300 DPI

```html
<!DOCTYPE html>
<html lang="en">
<head>
<meta charset="utf-8">
<title>Kelvara North Audit &amp; Compliance – Business Card</title>
<link rel="stylesheet" href="https://fonts.googleapis.com/css2?family=Arimo&family=Open+Sans&display=swap">
<style>
  :root {
    --paper: #ffffff;
    --front-yellow: #ecf90b;
    --map-yellow: #fadc02;
    --ink-dark: #2b2a26;
    --accent-orange: #f06a12;
    --back-orange: #fa4108;
    --back-cyan: #4be6f5;
    --divider-yellow: #f5d400;
    --text-light: #ffffff;
    --crop: #000000;
  }
  * { margin: 0; padding: 0; box-sizing: border-box; }
  html, body { width: 976px; height: 1200px; overflow: hidden; background: var(--paper); }
  .sheet { position: relative; width: 976px; height: 1200px; }

  .crop-marks { position: absolute; inset: 0; }

  .card-front {
    position: absolute; left: 21px; top: 20px; width: 928px; height: 537px;
    background: var(--front-yellow); overflow: hidden;
  }
  .map-backdrop {
    position: absolute; left: 330px; top: -10px; width: 620px; height: 560px;
    background: var(--map-yellow); border-radius: 38% 12% 30% 45%;
  }
  .brand-dot {
    position: absolute; left: 200px; top: 250px; width: 96px; height: 96px;
    border-radius: 50%; background: var(--accent-orange);
  }
  .brand-name {
    position: absolute; left: 380px; top: 258px; width: 500px;
    font-family: "Arimo", Arial, sans-serif; font-weight: 400; color: var(--ink-dark);
    font-size: 30px; line-height: 40px; text-align: left;
  }

  .card-back {
    position: absolute; left: 21px; top: 642px; width: 928px; height: 537px;
    background: var(--back-orange); overflow: hidden;
    font-family: "Arimo", Arial, sans-serif; color: var(--text-light);
  }
  .person { position: absolute; left: 74px; top: 153px; }
  .person-name { font-size: 32px; line-height: 1; }
  .person-title { font-size: 25px; margin-top: 14px; line-height: 1; }
  .person-mobile { font-size: 27px; margin-top: 12px; display: flex; align-items: center; gap: 4px; line-height: 1; }

  .column-rule {
    position: absolute; left: 386px; top: 117px; width: 2px; height: 263px;
    background: var(--divider-yellow);
  }
  .contact { position: absolute; left: 461px; top: 157px; font-size: 24px; }
  .address { font-style: normal; line-height: 37px; }
  .contact-row { display: flex; align-items: center; margin-top: 9px; height: 36px; }
  .contact-row svg { flex: none; }
  .phone-row span { margin-left: 22px; font-size: 25px; }
  .email-row span { margin-left: 26px; font-size: 25px; }

  .web-band {
    position: absolute; left: 0; bottom: 0; width: 100%; height: 103px;
    background: var(--back-cyan); display: flex; align-items: center; justify-content: center;
    font-family: "Open Sans", sans-serif; font-size: 23px; letter-spacing: 4.5px; color: var(--text-light);
  }
</style>
</head>
<body>
<div class="sheet">

  <section class="card-front">
    <div class="map-backdrop" role="img" aria-label="Large map of Australia in warm yellow as background decoration"></div>
    <div class="brand-dot"></div>
    <h1 class="brand-name">Kelvara North<br>Audit &amp; Compliance</h1>
  </section>

  <section class="card-back">
    <div class="person">
      <div class="person-name">Maren Holt</div>
      <div class="person-title">Director</div>
      <div class="person-mobile">
        <svg width="22" height="30" viewBox="0 0 22 30" aria-hidden="true">
          <rect x="2" y="2" width="18" height="26" rx="3" fill="none" stroke="#fff" stroke-width="2.4"/>
          <circle cx="7" cy="23" r="1.4" fill="#fff"/><circle cx="11" cy="23" r="1.4" fill="#fff"/><circle cx="15" cy="23" r="1.4" fill="#fff"/>
        </svg>
        <span>+61400 512 638</span>
      </div>
    </div>

    <div class="column-rule"></div>

    <div class="contact">
      <address class="address">48 Brindle Street<br>HOLLOWAY TAS 7012<br>Australia</address>
      <div class="contact-row phone-row">
        <svg width="38" height="28" viewBox="0 0 38 28" aria-hidden="true">
          <path d="M2 11 C2 3 36 3 36 11 L36 14 L27 14 L27 10 L11 10 L11 14 L2 14 Z" fill="#fff"/>
          <path d="M9 14 L29 14 L34 26 L4 26 Z" fill="#fff"/>
          <circle cx="19" cy="19" r="4.5" fill="var(--back-orange)"/>
        </svg>
        <span>+61362 508 114</span>
      </div>
      <div class="contact-row email-row">
        <svg width="36" height="26" viewBox="0 0 36 26" aria-hidden="true">
          <rect x="2" y="2" width="32" height="22" rx="2" fill="none" stroke="#fff" stroke-width="2.4"/>
          <path d="M2 3 L18 15 L34 3 M2 23 L14 12 M34 23 L22 12" fill="none" stroke="#fff" stroke-width="2.4"/>
        </svg>
        <span>xxxxxxxxxxxxx@mailbox.com</span>
      </div>
    </div>

    <div class="web-band">www.kelvaranorth.com.au</div>
  </section>

  <svg class="crop-marks" width="976" height="1200" viewBox="0 0 976 1200" aria-hidden="true">
    <g stroke="var(--crop)" stroke-width="1.2">
      <line x1="37" y1="0" x2="37" y2="24"/><line x1="0" y1="35" x2="24" y2="35"/>
      <line x1="936" y1="0" x2="936" y2="24"/><line x1="952" y1="35" x2="976" y2="35"/>
      <line x1="37" y1="550" x2="37" y2="572"/><line x1="0" y1="541" x2="24" y2="541"/>
      <line x1="936" y1="550" x2="936" y2="572"/><line x1="952" y1="541" x2="976" y2="541"/>
      <line x1="37" y1="622" x2="37" y2="646"/><line x1="0" y1="657" x2="24" y2="657"/>
      <line x1="936" y1="622" x2="936" y2="646"/><line x1="952" y1="657" x2="976" y2="657"/>
      <line x1="37" y1="1176" x2="37" y2="1200"/><line x1="0" y1="1165" x2="24" y2="1165"/>
      <line x1="936" y1="1176" x2="936" y2="1200"/><line x1="952" y1="1165" x2="976" y2="1165"/>
    </g>
  </svg>

</div>
</body>
</html>
```